Large multi-office optometry business opening a Dry Eye Spa and needs sign.

Business name/sign info: Brenwick Dry Eye Institute, (555) 362-4817
Backlit pole sign at office entrance on a very busy street
Sign dimensions: 53" tall x 136.5" wide
State of the art Dry Eye Spa for treatment of all forms of dry eye and ocular surface disease. Also, have aesthetics treatments (IPL, Low Level Light Treatment, etc.)

Target Market(s)

People who are suffering from: dryness, burning, foreign body sensation, itching, fluctuating vision, tired eyes, etc.

Industry/Entity Type

Optometry and aesthetics

Colors
0054AA
0677BA
7BADD7
CADEEF
E8F1F8

Requirements
Must have
• Business name, phone number, subliminal message of relief in a glance or short look.
Nice to have
• Cool, relief, soothing sense.
Should not have
• Too much information or too busy.

```html
<!DOCTYPE html>
<html lang="en">
<head>
<meta charset="utf-8">
<title>Brenwick Dry Eye Institute – Pole Sign</title>
<link rel="stylesheet" href="https://fonts.googleapis.com/css2?family=Anton&family=Montserrat:wght@800&display=swap">
<style>
  :root {
    --page-bg: #e8f1f8;
    --sign-blue-top: #0677ba;
    --sign-blue: #0054aa;
    --band-navy: #0a2487;
    --panel-light: #2a8ad0;
    --text-white: #ffffff;
  }
  * { margin: 0; padding: 0; box-sizing: border-box; }
  html, body {
    width: 1200px;
    height: 904px;
    overflow: hidden;
    background: var(--page-bg);
  }
  .canvas {
    position: relative;
    width: 1200px;
    height: 904px;
    display: flex;
    align-items: center;
    justify-content: center;
  }
  .sign {
    position: relative;
    width: 1100px;
    height: 427px;
    overflow: hidden;
    background: linear-gradient(180deg, var(--sign-blue-top) 0%, var(--sign-blue) 70%);
    box-shadow: 0 10px 30px rgba(0, 40, 90, 0.18);
  }
  .sign-title {
    position: absolute;
    left: 52px;
    top: 22px;
    font-family: "Anton", "Impact", sans-serif;
    font-weight: 400;
    font-size: 132px;
    line-height: 0.98;
    letter-spacing: 1px;
    color: var(--text-white);
    text-transform: uppercase;
    white-space: nowrap;
    z-index: 2;
  }
  .sign-title span { display: block; }
  .drop-art {
    position: absolute;
    right: 0;
    top: 0;
    width: 240px;
    height: 290px;
    background: linear-gradient(180deg, var(--sign-blue-top) 0%, var(--panel-light) 100%);
  }
  .contact-band {
    position: absolute;
    left: 0;
    right: 0;
    bottom: 0;
    height: 137px;
    background: var(--band-navy);
    display: flex;
    align-items: center;
    padding-left: 52px;
    z-index: 1;
  }
  .contact-phone {
    font-family: "Montserrat", "Arial Black", sans-serif;
    font-weight: 800;
    font-size: 88px;
    letter-spacing: 1px;
    color: var(--text-white);
    white-space: nowrap;
  }
</style>
</head>
<body>
  <main class="canvas">
    <section class="sign" aria-label="Brenwick Dry Eye Institute pole sign">
      <h1 class="sign-title">
        <span>Brenwick Dry</span>
        <span>Eye Institute</span>
      </h1>
      <div class="drop-art" role="img" aria-label="Illustration of a water droplet over rippling water belongs here"></div>
      <div class="contact-band">
        <p class="contact-phone">CALL: (555) 362-4817</p>
      </div>
    </section>
  </main>
</body>
</html>
```